Web Design Project

Hi everyone

Thanks for taking the time to read about this project.

Website needed for Lorel, female singer/songwriter and performer who is launching her debut album this year. She writes and performs folk/pop/soft rock music and plays guitar and piano.

see vidplexa links for examples of Lorel's style:
http://www.vidplexa.com/watch?v=qTbn4Zr8Lp2
http://www.vidplexa.com/watch?v=Kovd7wUheJm

Looking for a classy, modern feel to the website. Cool colours are preferred but open to ideas. It needs it to have CoinDrop set up so items can be purchased from the site. The theme will be continued to Chatterbook and business cards.

Examples include:

http://www.bettyculverdale.com/

http://tessafordyce.com/

http://www.juneqtunes.com/home

Pages and content to be included:

HOME - main picture and general content

BIO - written content about Lorel

NEWS - this will be regularly updated, blog style

GIGS - this will be regularly updated

GALLERY - content will be photos only

SEE AND HEAR - content will be Videos and audios

STORE - this will have a coindrop function for purchase of CD and merchandise

GENEROSITY - this page will be devoted to charity work and updated regularly

CONTACT - information on how to contact Lorel's management

Buttons will need to provide links to Vidplexa, Chirpline, Chatterbook, Snapgrove

I will work closely with the designers in giving feedback as ideas are generated and then provide further content such as photos and videos.

Thanks for considering this project!
Updates

HI everyone thanks for all your submissions so far. Please note the following:

- photos have been uploaded to assist with themes

- background could be a solid colour or texture (e.g. tree trunk texture)

- please use a hand writing font similar to Google font "Give You Glory" - doesn't have to be exactly this but similar

Thank you,

Lorel

Hi again everyone

I apologise but the pixel guild website won't allow me to upload files. I will attempt to correct this as soon as possible. Thanks                                   

18-55 year olds who appreciate this genre of music; gay and lesbian community

Charity

• No flowers or flowery themes

```html
<!DOCTYPE html>
<html lang="en">
<head>
<meta charset="utf-8">
<title>Lorel — Singer</title>
<link rel="stylesheet" href="https://fonts.googleapis.com/css2?family=Bitter:wght@700&family=Ubuntu:wght@500&display=swap">
<style>
  :root {
    --accent: #e0672c;
    --ink: #3b3833;
    --body-text: #2a2a28;
    --header-bg: #fdfaef;
    --page-bg: #e9e1c3;
    --stripe: #e4dbb9;
    --frame: #dcd1a8;
    --rule: #f7f1dc;
    --footer-bg: #ffffff;
  }
  * { margin: 0; padding: 0; box-sizing: border-box; }
  html, body { width: 900px; height: 1200px; overflow: hidden; }
  body {
    position: relative;
    font-family: Arial, Helvetica, sans-serif;
    color: var(--body-text);
    background: repeating-linear-gradient(90deg, var(--page-bg) 0 20px, var(--stripe) 20px 40px);
  }

  .site-header {
    position: absolute; left: 0; top: 0; width: 900px; height: 146px;
    background: var(--header-bg);
    border-top: 4px solid var(--accent);
  }
  .header-edge, .footer-edge {
    position: absolute; left: 0; width: 900px; height: 5px;
    background-size: 8px 5px; background-repeat: repeat-x;
  }
  .header-edge { top: 146px; background-image: radial-gradient(circle at 4px 0, var(--header-bg) 4px, transparent 4.5px); }
  .footer-edge { top: 1115px; background-image: radial-gradient(circle at 4px 5px, var(--footer-bg) 4px, transparent 4.5px); }

  .brand-rule {
    position: absolute; top: 51px; height: 5px;
    border-top: 2px solid #e7dfc0; border-bottom: 1px solid #e7dfc0;
  }
  .brand-rule.left { left: 90px; width: 298px; }
  .brand-rule.right { left: 544px; width: 280px; }
  .brand {
    position: absolute; left: 388px; width: 156px; top: 22px; text-align: center;
    font-family: 'Bitter', Georgia, serif; font-weight: 700; font-size: 40px;
    color: var(--accent); line-height: 1;
  }

  .main-nav {
    position: absolute; left: 90px; top: 110px; width: 718px; height: 25px;
    display: flex; align-items: center; justify-content: space-between;
    font-family: 'Ubuntu', Arial, sans-serif; font-weight: 500; font-size: 11px;
    letter-spacing: 0.5px; color: #2c2a27;
  }
  .main-nav a { color: inherit; text-decoration: none; }
  .main-nav .sep { width: 1px; height: 15px; background: #ddd6bd; }
  .main-nav .current {
    background: var(--accent); color: #fff; border-radius: 3px;
    padding: 6px 9px; line-height: 13px;
  }

  .hero-frame {
    position: absolute; left: 94px; top: 164px; width: 712px; height: 308px;
    background: var(--frame); border-radius: 8px;
  }
  .hero-photo {
    position: absolute; left: 16px; top: 16px; width: 681px; height: 277px;
    background: linear-gradient(120deg, #1b2140 0%, #3a3a44 35%, #c8c6cc 55%, #1a1a1e 80%, #3a2b26 100%);
  }
  .slider-dots {
    position: absolute; left: 332px; top: 284px; width: 48px; height: 18px;
    background: var(--rule); border-radius: 9px;
    display: flex; gap: 2px; justify-content: center; align-items: center;
  }
  .slider-dots span { width: 10px; height: 10px; border-radius: 50%; background: #cdbf93; }
  .slider-dots span.active { background: var(--accent); }

  .welcome-title {
    position: absolute; left: 0; top: 492px; width: 900px; text-align: center;
    font-family: 'Bitter', Georgia, serif; font-weight: 700; font-size: 26px;
    color: var(--ink); letter-spacing: 0.5px;
  }
  .accent { color: var(--accent); }
  .welcome-text {
    position: absolute; left: 106px; top: 535px; width: 696px; text-align: center;
    font-size: 10.5px; line-height: 15px;
  }

  .divider { position: absolute; height: 2px; border-top: 1px solid #d8cea9; border-bottom: 1px solid var(--rule); }
  .divider.one { left: 94px; top: 613px; width: 710px; }
  .divider.two { left: 90px; top: 894px; width: 712px; }

  .section-title {
    position: absolute; left: 90px;
    font-family: 'Bitter', Georgia, serif; font-weight: 700; font-size: 22px;
    color: var(--ink); letter-spacing: 0.5px;
  }
  .testimonials-title { top: 633px; }
  .gallery-title { top: 903px; }

  .avatar {
    position: absolute; left: 93px; top: 673px; width: 52px; height: 61px;
    border: 2px solid #f6f0dc;
    background: linear-gradient(160deg, #4a2d25 0%, #8a3a2a 50%, #6d85b4 100%);
  }
  .quote-mark { position: absolute; font-family: Georgia, serif; font-size: 30px; color: #c9bb8f; line-height: 1; }
  .quote-mark.open { left: 149px; top: 670px; }
  .quote-mark.close { left: 151px; top: 819px; }
  .quote-lead {
    position: absolute; left: 170px; top: 671px; width: 256px;
    font-size: 10px; line-height: 14.3px; text-align: justify;
  }
  .quote-body {
    position: absolute; left: 90px; top: 748px; width: 336px;
    font-size: 10px; line-height: 14.3px; text-align: justify;
  }
  .quote-author {
    position: absolute; left: 226px; top: 842px; width: 200px; text-align: right;
    font-size: 10.5px; font-weight: bold; color: var(--accent);
  }

  .video-frame {
    position: absolute; left: 451px; top: 637px; width: 353px; height: 215px;
    border: 2px solid #f6f0dc;
    background: linear-gradient(110deg, #2c2c2c 0%, #707070 40%, #bdbdbd 65%, #454545 100%);
  }
  .play-button { position: absolute; left: 136px; top: 64px; }

  .gallery-frame {
    position: absolute; top: 950px; width: 215px; height: 139px;
    background: var(--frame); border-radius: 6px;
  }
  .gallery-frame .photo { position: absolute; left: 9px; top: 9px; width: 196px; height: 121px; }
  .gallery-frame.first { left: 90px; }
  .gallery-frame.second { left: 340px; }
  .gallery-frame.third { left: 590px; }
  .photo.stage { background: linear-gradient(135deg, #3a2b7a 0%, #6d4aa8 45%, #b46a8a 70%, #4c5fa0 100%); }
  .photo.keys { background: linear-gradient(120deg, #15151a 0%, #d0d0d4 45%, #1e1e22 75%, #2b1b18 100%); }
  .photo.portrait { background: linear-gradient(160deg, #5a1010 0%, #8e3a2a 45%, #c99a80 65%, #5f7fb0 100%); }

  .site-footer {
    position: absolute; left: 0; top: 1120px; width: 900px; height: 80px;
    background: var(--footer-bg); text-align: center;
  }
  .footer-nav {
    margin-top: 22px; font-size: 10.5px; color: #2c2a27;
    display: flex; justify-content: center; gap: 11px;
  }
  .footer-nav a { color: inherit; text-decoration: none; }
  .copyright { margin-top: 11px; font-size: 10.5px; color: #2c2a27; }
</style>
</head>
<body>
  <header class="site-header">
    <div class="brand-rule left"></div>
    <div class="brand">Lorel</div>
    <div class="brand-rule right"></div>
    <nav class="main-nav">
      <a class="current" href="#">HOME</a><span class="sep"></span>
      <a href="#">BIO</a><span class="sep"></span>
      <a href="#">NEWS</a><span class="sep"></span>
      <a href="#">GIGS</a><span class="sep"></span>
      <a href="#">GALLERY</a><span class="sep"></span>
      <a href="#">SEE AND HEAR</a><span class="sep"></span>
      <a href="#">STORE</a><span class="sep"></span>
      <a href="#">GENEROSITY</a><span class="sep"></span>
      <a href="#">CONTACT</a>
    </nav>
  </header>
  <div class="header-edge"></div>

  <section class="hero-frame">
    <div class="hero-photo" role="img" aria-label="Hands playing a grand piano keyboard"></div>
    <div class="slider-dots"><span class="active"></span><span></span><span></span></div>
  </section>

  <h1 class="welcome-title">Welcome to <span class="accent">Lorel</span> Official Website!</h1>
  <p class="welcome-text">Lorel is a singer-songwriter with an extraordinary ability to reach out to people with her musical gift. She performs her songs with beautiful emotion.simply dummy text of the printing and typesetting industry. Lorem Ipsum has been the industry's standard dummy text ever since the 1500s, when an unknown printer took a galley of type and scrambled it to make a type specimen book. It has survived not only five centuries, but also the leap into electronic typesetting,</p>

  <div class="divider one"></div>

  <h2 class="section-title testimonials-title">Testimonials</h2>
  <div class="avatar" role="img" aria-label="Small portrait photo of the reviewer"></div>
  <span class="quote-mark open">&ldquo;</span>
  <p class="quote-lead">simply dummy text of the printing and typesetting industry. Lorem Ipsum has been the industry's standard dummy text ever since the 1500s, when an un known printer took a galley of type and scrambled it to make a has been the industry's standard</p>
  <p class="quote-body">simply dummy text of the printing and typesetting industry. Lorem Ipsum has been the industry's standard dummy text ever since the 1500s, when an unknown printer took a galley of type and scrambled it to make a type specimen book. It has survived not only five centuries, but also the leap into electronic typesetting, remaining essentially unchanged. It was popularised in the 1960s.</p>
  <span class="quote-mark close">&rdquo;</span>
  <p class="quote-author">Posted by Evan Holt !</p>

  <div class="video-frame" role="img" aria-label="Black and white video still of the singer at a microphone">
    <svg class="play-button" width="80" height="80" viewBox="0 0 80 80">
      <circle cx="40" cy="40" r="38" fill="#ffffff" fill-opacity="0.35" stroke="#ffffff" stroke-opacity="0.6" stroke-width="2"/>
      <path d="M31 22 L60 40 L31 58 Z" fill="#2a2a2a"/>
    </svg>
  </div>

  <div class="divider two"></div>

  <h2 class="section-title gallery-title">Photo <span class="accent">Gallery</span></h2>
  <div class="gallery-frame first"><div class="photo stage" role="img" aria-label="Singer performing at a microphone under purple stage light"></div></div>
  <div class="gallery-frame second"><div class="photo keys" role="img" aria-label="Hands on piano keys"></div></div>
  <div class="gallery-frame third"><div class="photo portrait" role="img" aria-label="Smiling portrait of the singer against a red background"></div></div>

  <div class="footer-edge"></div>
  <footer class="site-footer">
    <nav class="footer-nav">
      <a href="#">Home</a><span>~</span>
      <a href="#">Bio</a><span>~</span>
      <a href="#">News</a><span>~</span>
      <a href="#">Gigs</a><span>~</span>
      <a href="#">Gallery</a><span>~</span>
      <a href="#">See And Hear</a><span>~</span>
      <a href="#">Store</a><span>~</span>
      <a href="#">Generosity</a><span>~</span>
      <a href="#">Contact</a>
    </nav>
    <p class="copyright">&copy; 2013 Powered By Shopvale&trade;. All Rights Reserved</p>
  </footer>
</body>
</html>
```